Verdant Ledger - Paid Surveys publisher portal

• Homepage
• Blank Sub Page (Where content goes in between the header/footer)
• Publisher Application Page, complete with Form
• Survey Wall page

Sites that are in a similar vertical that have interesting designs:
mobrivex.com
tandulo.com
vorql.com
pim.ox

This is a business-to-business site, and needs to have this type of feel to it. Focus on generating revenue, offer completion, paid surveys is the market.

Format: HTML/CSS

Link to current version of application, and form:
https://quorbit.travenlo.com
https://quorbit.travenlo.com/apply
https://quorbit.travenlo.com/panel/4/mirvak_user

Please note that we are changing the brand of this project, the name will be determined shortly but everything else remains. It will likely be Verdant Ledger instead of Quorbit. We will confirm.

Industry/Entity Type

Market Research

Coding

Coded - Design and coding required

Number of Pages Required

4 page

Font styles to use
Sans Serif

Colors

Designer to choose colors to be used in the design.

```html
<!DOCTYPE html>
<html lang="en">
<head>
<meta charset="utf-8">
<title>Verdant Ledger – Publisher Application</title>
<link href="https://fonts.googleapis.com/css2?family=Roboto:wght@300;400;500;700&family=Roboto+Condensed:wght@400;700&display=swap" rel="stylesheet">
<style>
:root{
  --ink:#0b0b0b;
  --brand:#1a3d8f;
  --brand-line:#173a92;
  --white:#ffffff;
  --text:#333333;
  --label:#444444;
  --field-border:#d6d6d6;
  --placeholder:#8a8a8a;
  --footer:#262626;
  --footer-text:#9a9a9a;
}
*{box-sizing:border-box;margin:0;padding:0}
html,body{width:1038px;height:1200px;overflow:hidden;background:var(--white);font-family:'Roboto',sans-serif;color:var(--text)}
.page{position:relative;width:1038px;height:1200px}

.site-header{position:absolute;left:0;top:0;width:1038px;height:74px;background:var(--ink)}
.brand{position:absolute;left:158px;top:18px}
.brand-name{display:block;font-family:'Roboto Condensed',sans-serif;font-weight:700;font-size:17px;line-height:19px;color:var(--white);text-transform:uppercase;width:110px}
.main-nav{position:absolute;top:0;left:402px;height:74px;display:flex}
.nav-item{position:relative;height:74px;line-height:72px;font-family:'Roboto Condensed',sans-serif;font-weight:700;font-size:12px;color:var(--white);text-transform:uppercase;white-space:nowrap}
.nav-item.home{width:62px}
.nav-item.apply{width:143px;text-align:center}
.nav-item.apply::after{content:"";position:absolute;left:0;right:0;bottom:2px;height:3px;background:var(--white)}
.nav-item.survey{margin-left:22px}
.caret{display:inline-block;width:5px;height:5px;border-right:1.5px solid var(--white);border-bottom:1.5px solid var(--white);transform:rotate(45deg);margin-left:5px;vertical-align:3px}
.account{position:absolute;left:764px;top:0;height:70px;line-height:70px;font-family:'Roboto Condensed',sans-serif;font-size:12px;color:var(--white);display:flex;align-items:center;gap:5px}
.search{position:absolute;left:877px;top:28px}

.hero{position:absolute;left:0;top:74px;width:1038px;height:164px;background:linear-gradient(100deg,#6d6f72 0%,#8b8c8e 30%,#7a7b7d 60%,#5e6063 100%);text-align:center;color:var(--white)}
.hero-title{position:absolute;left:0;right:0;top:41px;font-weight:300;font-size:32px;letter-spacing:.3px}
.hero-sub{position:absolute;left:0;right:0;top:89px;font-weight:500;font-size:16px}

.apply-card{position:absolute;left:148px;top:289px;width:738px;height:719px;border:3px solid var(--brand-line);background:var(--white);box-shadow:0 10px 28px rgba(0,0,0,.28)}
.apply-title{position:absolute;left:0;right:0;top:38px;text-align:center;font-weight:300;font-size:31px;color:#111;letter-spacing:.3px}
.apply-form{position:absolute;left:62px;top:129px;width:615px;display:grid;grid-template-columns:296px 298px;column-gap:21px}
.field{height:79px}
.field-label{display:block;font-size:12px;color:var(--label);height:22px}
.field-input{display:block;width:100%;height:33px;border:1px solid var(--field-border);padding:0 10px;font-size:10px;color:var(--placeholder);line-height:31px;position:relative}
.field.indent .field-label{padding-left:11px}
.field-input.select::after{content:"";position:absolute;right:14px;top:11px;width:6px;height:6px;border-right:1.3px solid #555;border-bottom:1.3px solid #555;transform:rotate(45deg)}
.submit-button{position:absolute;left:62px;top:602px;width:615px;height:40px;background:var(--brand);color:var(--white);font-weight:500;font-size:12px;letter-spacing:.3px;text-align:center;line-height:40px;text-transform:uppercase}

.site-footer{position:absolute;left:0;top:1058px;width:1038px;height:142px;background:var(--footer);text-align:center}
.back-top{position:absolute;left:505px;top:-13px;width:28px;height:28px;border-radius:50%;background:#1d1d1d}
.footer-links{position:absolute;left:0;right:0;top:34px;font-family:'Roboto Condensed',sans-serif;font-size:11px;color:var(--footer-text)}
.social{position:absolute;left:507px;top:68px;display:flex;gap:12px}
.social span{width:9px;height:9px;border-radius:50%;background:var(--white)}
.copyright{position:absolute;left:0;right:0;top:103px;font-size:10px;color:#7d7d7d}
</style>
</head>
<body>
<div class="page">
  <header class="site-header">
    <div class="brand"><span class="brand-name">Verdant Ledger</span></div>
    <nav class="main-nav">
      <span class="nav-item home">Home<span class="caret"></span></span>
      <span class="nav-item apply">Publisher Application</span>
      <span class="nav-item survey">Survey</span>
    </nav>
    <div class="account">
      <svg width="10" height="10" viewBox="0 0 10 10"><circle cx="5" cy="3" r="2.4" fill="#fff"/><path d="M0.5 10c0-3 2-4.5 4.5-4.5S9.5 7 9.5 10z" fill="#fff"/></svg>
      <span>Login / Signup</span><span class="caret"></span>
    </div>
    <svg class="search" width="12" height="12" viewBox="0 0 12 12"><circle cx="5" cy="5" r="3.6" fill="none" stroke="#fff" stroke-width="1.8"/><line x1="7.6" y1="7.6" x2="11" y2="11" stroke="#fff" stroke-width="2"/></svg>
  </header>

  <section class="hero" role="img" aria-label="Photo of hands typing on a laptop keyboard on a desk">
    <h1 class="hero-title">Start Generating Revenue</h1>
    <p class="hero-sub">Publisher Application</p>
  </section>

  <main class="apply-card">
    <h2 class="apply-title">Apply to Become a Publisher</h2>
    <div class="apply-form">
      <div class="field"><span class="field-label">First Name</span><span class="field-input">First Name ....</span></div>
      <div class="field"><span class="field-label">Last Name</span><span class="field-input">Last Name ....</span></div>
      <div class="field"><span class="field-label">Email</span><span class="field-input">Email ....</span></div>
      <div class="field"><span class="field-label">Address</span><span class="field-input">Address ....</span></div>
      <div class="field"><span class="field-label">City</span><span class="field-input">City....</span></div>
      <div class="field"><span class="field-label">State</span><span class="field-input">State ....</span></div>
      <div class="field"><span class="field-label">Zipcode</span><span class="field-input">Zipcode....</span></div>
      <div class="field"><span class="field-label">Country</span><span class="field-input select">Afghanistan</span></div>
      <div class="field"><span class="field-label">Telephone</span><span class="field-input">Telephone....</span></div>
      <div class="field"><span class="field-label">Username</span><span class="field-input">Username....</span></div>
      <div class="field indent"><span class="field-label">Website Name</span><span class="field-input">Website Name....</span></div>
      <div class="field"><span class="field-label">Website Url</span><span class="field-input">Website Url....</span></div>
    </div>
    <div class="submit-button">Submit Application</div>
  </main>

  <footer class="site-footer">
    <div class="back-top"><svg width="28" height="28" viewBox="0 0 28 28"><path d="M10 16l4-4 4 4" fill="none" stroke="#fff" stroke-width="1.6"/></svg></div>
    <div class="footer-links">Home | Publisher | Survey</div>
    <div class="social" aria-label="Social links"><span></span><span></span></div>
    <div class="copyright">©Copyright information here</div>
  </footer>
</div>
</body>
</html>
```